Business Card Design Project

Hello
I want a Simple Business card that uses the company logo that is easily reasonable but looks professional as I am an IT Services company and would look to share these cards with prospective clients.
The details are:
Kestrel Arc Solutions
14 Morrow Lane
Birmingham
B7 4QX
Telephone 0845 217 6640
I would like my name Oliver Hastings and my title Director on the card.
Target Market(s)
IT Professionals
Industry/Entity Type
Business

```html
<!DOCTYPE html>
<html lang="en">
<head>
<meta charset="utf-8">
<title>Kestrel Arc Solutions – Business Card Options</title>
<link rel="stylesheet" href="https://fonts.googleapis.com/css2?family=Poppins:wght@400;600&family=Questrial&display=swap">
<style>
  :root {
    --backdrop: #2c2c2c;
    --backdrop-edge: #1f1f1f;
    --card: #fbfbfa;
    --ink: #1d1d1b;
    --accent: #6aa23c;
    --leaf-light: #d6e25a;
    --leaf-mid: #9fcc4a;
    --leaf-deep: #58a83f;
    --divider: #8fbf6a;
  }
  * { box-sizing: border-box; margin: 0; padding: 0; }
  html, body { width: 1200px; height: 1200px; overflow: hidden; }
  body {
    background: radial-gradient(circle at 50% 45%, var(--backdrop) 0%, var(--backdrop-edge) 100%);
    position: relative;
    font-family: "Questrial", sans-serif;
  }
  .option-number {
    position: absolute;
    left: 136px;
    font-family: "Poppins", sans-serif;
    font-weight: 600;
    font-size: 96px;
    line-height: 1;
    color: var(--accent);
  }
  .option-number--three { top: 196px; }
  .option-number--four { top: 666px; }

  .card {
    position: absolute;
    left: 322px;
    width: 556px;
    height: 344px;
    background: var(--card);
    overflow: hidden;
  }
  .card--three { top: 202px; }
  .card--four { top: 672px; }

  .card__decoration {
    position: absolute;
    right: 0;
    top: 0;
    width: 150px;
    height: 340px;
    border-radius: 75px 0 0 40px;
    background: linear-gradient(160deg, var(--leaf-mid) 0%, var(--leaf-light) 45%, var(--leaf-deep) 100%);
    opacity: 0.85;
  }

  .card__identity {
    position: absolute;
    left: 28px;
    top: 186px;
    display: flex;
    align-items: flex-end;
  }
  .brand {
    display: flex;
    align-items: center;
    gap: 8px;
    width: 188px;
    font-family: "Poppins", sans-serif;
    font-weight: 600;
    font-size: 27px;
    line-height: 1;
    color: var(--ink);
    letter-spacing: -0.5px;
  }
  .brand__dot {
    width: 14px;
    height: 14px;
    border-radius: 50%;
    background: var(--accent);
    flex: none;
  }
  .card__divider {
    width: 1px;
    height: 46px;
    background: var(--divider);
    margin-right: 9px;
  }
  .person { display: flex; flex-direction: column; }
  .person__name {
    font-family: "Poppins", sans-serif;
    font-weight: 600;
    font-size: 29px;
    line-height: 1;
    color: var(--ink);
    letter-spacing: -0.3px;
  }
  .person__title {
    font-size: 10px;
    line-height: 1;
    color: var(--ink);
    letter-spacing: 1px;
    margin-top: 2px;
  }
  .contact {
    position: absolute;
    right: 34px;
    top: 264px;
    text-align: right;
    font-size: 14px;
    line-height: 22px;
    color: var(--ink);
  }
</style>
</head>
<body>
  <div class="option-number option-number--three">3</div>
  <section class="card card--three">
    <div class="card__decoration" role="img" aria-label="Large soft green foliage shapes decorating the right edge of the card"></div>
    <div class="card__identity">
      <div class="brand"><span class="brand__dot"></span>kestrel arc</div>
      <div class="card__divider"></div>
      <div class="person">
        <span class="person__name">oliver hastings</span>
        <span class="person__title">director</span>
      </div>
    </div>
    <address class="contact" style="font-style:normal">
      14 Morrow Lane, Birmingham B7 4QX<br>0845 217 6640
    </address>
  </section>

  <div class="option-number option-number--four">4</div>
  <section class="card card--four">
    <div class="card__identity">
      <div class="brand"><span class="brand__dot"></span>kestrel arc</div>
      <div class="card__divider"></div>
      <div class="person">
        <span class="person__name">oliver hastings</span>
        <span class="person__title">director</span>
      </div>
    </div>
    <address class="contact" style="font-style:normal">
      14 Morrow Lane, Birmingham B7 4QX<br>0845 217 6640
    </address>
  </section>
</body>
</html>
```